TLR Property - Business Cards

Looking for a business card & general letterhead, signage etc design for our new logo.

Colours:
000a20
0056a2
00b5ef
0088ce
68cef2

Fonts:
Poppins
Karla

Please keep look and feel of new brand - example in the zip package I sent.

```html
<!DOCTYPE html>
<html lang="en">
<head>
<meta charset="utf-8">
<title>TLR Property – Business Cards</title>
<link href="https://fonts.googleapis.com/css2?family=Montserrat:wght@400;500;600&family=Patrick+Hand&display=swap" rel="stylesheet">
<style>
  :root {
    --backdrop: #9a9a9a;
    --paper: #ffffff;
    --brand-blue: #0b57a5;
    --mid-blue: #1a88ca;
    --ink: #2a2a2a;
    --title-ink: #1a1a1a;
  }
  * { margin: 0; padding: 0; box-sizing: border-box; }
  html, body {
    width: 1093px; height: 1200px; overflow: hidden;
    background: var(--backdrop);
    font-family: "Montserrat", sans-serif;
  }
  .canvas { position: relative; width: 1093px; height: 1200px; }

  .card {
    position: absolute; left: 264px; width: 581px; height: 364px;
    border-radius: 18px; overflow: hidden;
  }
  .card--front { top: 225px; background: var(--paper); }
  .card--back  { top: 616px; background: var(--brand-blue); }

  .wordmark {
    position: absolute; left: 23px; top: 40px;
    font-weight: 600; font-size: 38px; letter-spacing: 0.5px;
    color: var(--brand-blue); line-height: 1;
  }
  .wordmark--reverse {
    left: 0; right: 0; top: 158px; text-align: center;
    font-size: 54px; color: var(--paper);
  }

  .holder { position: absolute; right: 35px; top: 28px; text-align: right; }
  .holder__name {
    font-family: "Patrick Hand", cursive;
    font-size: 28px; color: var(--brand-blue); line-height: 1.05;
  }
  .holder__title { font-size: 13px; font-weight: 500; color: var(--title-ink); margin-top: 2px; }
  .accent-bar {
    position: absolute; right: 0; top: 27px; width: 20px; height: 46px;
    background: var(--brand-blue);
  }

  .address {
    position: absolute; left: 24px; top: 201px;
    font-size: 14px; line-height: 16px; color: var(--ink);
  }

  .contacts { position: absolute; left: 26px; top: 267px; list-style: none; }
  .contacts li {
    display: flex; align-items: center; gap: 9px;
    height: 24.5px; font-size: 13.5px; color: var(--ink);
  }
  .contacts svg { width: 14px; height: 14px; fill: var(--mid-blue); flex: none; }
</style>
</head>
<body>
<main class="canvas">

  <section class="card card--front" aria-label="Business card front">
    <div class="wordmark">TLR Property</div>

    <div class="holder">
      <div class="holder__name">Dana Whitfield</div>
      <div class="holder__title">Managing Director</div>
    </div>
    <div class="accent-bar"></div>

    <address class="address" style="font-style:normal">
      42 Birch Hollow Lane<br>Ridgeton, MS 39000
    </address>

    <ul class="contacts">
      <li>
        <svg viewBox="0 0 24 24" aria-hidden="true"><path d="M6.6 10.8a15.1 15.1 0 0 0 6.6 6.6l2.2-2.2a1 1 0 0 1 1-.25 11.4 11.4 0 0 0 3.6.57 1 1 0 0 1 1 1V20a1 1 0 0 1-1 1A17 17 0 0 1 3 4a1 1 0 0 1 1-1h3.5a1 1 0 0 1 1 1c0 1.25.2 2.45.57 3.57a1 1 0 0 1-.25 1z"/></svg>
        555.010.4821
      </li>
      <li>
        <svg viewBox="0 0 24 24" aria-hidden="true"><path d="M2 5h20v2l-10 6L2 7z"/><path d="M2 9l10 6 10-6v10H2z"/></svg>
        info@tlrproperty.com
      </li>
      <li>
        <svg viewBox="0 0 24 24" aria-hidden="true"><circle cx="12" cy="12" r="10"/><path d="M7 6c2 1 3 3 2 5s-3 2-3 4 2 3 3 4M15 4c-1 2 0 3 2 4s3 3 2 6" stroke="#fff" stroke-width="1.6" fill="none"/></svg>
        www.tlrproperty.com
      </li>
    </ul>
  </section>

  <section class="card card--back" aria-label="Business card back">
    <div class="wordmark wordmark--reverse">TLR Property</div>
  </section>

</main>
</body>
</html>
```